Clean Plinth Ads Banner Design For A Finance Company

Hi,
We're a UK based finance company and are looking for new banner ads to use on the Plinth Display Network.
We want the end product to stand out by using strong, minimal design - ideally starting from a dark theme, although I'm open to ideas.
The copy should read:
'Fast Bridging Loans From 0.39% PM'
Once we have these designs agreed, we are looking to replicate them for other products, changing only the text on each ad - for example, 'commercial mortgage service you can rely on' or 'development finance service you can rely on'.
The colours used on our website are the following:
Black - #040303
Orange - #f79124
White - #ffffff
Grey - #ffffff
Example ads that I like - https://www.brimcastle.com/wp-content/uploads/2021/07/plinth-display-ads-example-2-final.png.webp
2 - https://quendrahub.com/wp-content/uploads/2020/03/fbdd56ba3bd16c7a8debb13a411de786.jpg

```html
<!DOCTYPE html>
<html lang="en">
<head>
<meta charset="utf-8">
<title>Orvane Finance – Display Banner Set</title>
<link href="https://fonts.googleapis.com/css2?family=Poppins:wght@400;600&display=swap" rel="stylesheet">
<style>
  :root {
    --black: #040303;
    --charcoal: #222222;
    --orange: #f79124;
    --white: #ffffff;
    --page: #ffffff;
  }
  * { margin: 0; padding: 0; box-sizing: border-box; }
  html, body { width: 1200px; height: 1143px; overflow: hidden; background: var(--page); }
  body { position: relative; font-family: "Poppins", sans-serif; color: var(--white); }

  .ad { position: absolute; overflow: hidden; box-shadow: 0 6px 16px rgba(0,0,0,0.18); }
  .brand {
    font-family: "Poppins", sans-serif; font-weight: 600; color: var(--orange);
    display: flex; align-items: center; gap: 8px; line-height: 1; white-space: nowrap;
  }
  .brand-dot { border-radius: 50%; background: var(--orange); flex: none; }
  .headline, .subline { font-weight: 400; white-space: nowrap; }

  /* Leaderboard */
  .ad-leaderboard { left: 67px; top: 51px; width: 1065px; height: 132px; background: var(--black); }
  .ad-leaderboard .photo {
    position: absolute; right: 0; top: 0; width: 760px; height: 132px;
    background: linear-gradient(90deg, #16324a 0%, #2b5f85 45%, #1a2c3e 100%);
    clip-path: polygon(236px 0, 100% 0, 100% 100%, 0 100%);
  }
  .ad-leaderboard .stripe { position: absolute; left: 0; top: 0; }
  .ad-leaderboard .brand { position: absolute; left: 18px; top: 14px; font-size: 18px; }
  .ad-leaderboard .brand-dot { width: 11px; height: 11px; }
  .ad-leaderboard .headline { position: absolute; left: 18px; top: 60px; font-size: 18px; }
  .ad-leaderboard .subline { position: absolute; left: 18px; top: 92px; font-size: 18px; }

  /* Rectangle */
  .ad-rectangle { left: 67px; top: 215px; width: 492px; height: 333px; }
  .ad-rectangle .photo {
    position: absolute; inset: 0;
    background: radial-gradient(ellipse at 70% 65%, #3c4a55 0%, #262d33 55%, #1a1d20 100%);
  }
  .ad-rectangle .content { position: absolute; inset: 0; text-align: center; }
  .ad-rectangle .brand { position: absolute; left: 0; right: 0; top: 48px; justify-content: center; font-size: 30px; }
  .ad-rectangle .brand-dot { width: 14px; height: 14px; }
  .ad-rectangle .headline { position: absolute; left: 0; right: 0; top: 128px; font-size: 18px; }
  .ad-rectangle .subline { position: absolute; left: 0; right: 0; top: 160px; font-size: 18px; }
  .ad-rectangle .phone {
    position: absolute; left: 0; right: 0; top: 283px; font-size: 18px;
    display: flex; justify-content: center; align-items: center; gap: 8px;
  }

  /* Skyscraper */
  .ad-skyscraper { left: 597px; top: 215px; width: 439px; height: 878px; background: var(--charcoal); }
  .ad-skyscraper .corner { position: absolute; right: 0; top: 0; }
  .ad-skyscraper .brand { position: absolute; left: 0; right: 0; top: 82px; justify-content: center; font-size: 34px; }
  .ad-skyscraper .brand-dot { width: 16px; height: 16px; }
  .ad-skyscraper .headline { position: absolute; left: 0; right: 0; top: 168px; text-align: center; font-size: 20px; }
  .ad-skyscraper .subline { position: absolute; left: 0; right: 0; top: 209px; text-align: center; font-size: 20px; }
  .ad-skyscraper .dots-area {
    position: absolute; left: 30px; top: 278px; width: 210px; height: 150px;
    background: linear-gradient(135deg, rgba(255,255,255,0) 40%, rgba(255,255,255,0.35) 100%);
    clip-path: polygon(100% 0, 100% 100%, 0 100%);
  }
  .ad-skyscraper .accent { position: absolute; left: 46px; top: 320px; }
  .ad-skyscraper .person {
    position: absolute; left: 4px; top: 400px; width: 435px; height: 478px;
    background: linear-gradient(180deg, #2d3138 0%, #8fa6c2 60%, #5c6c82 100%);
    clip-path: ellipse(55% 70% at 60% 100%);
  }

  /* Standalone name mark */
  .brand-standalone { position: absolute; left: 98px; top: 800px; font-size: 50px; }
  .brand-standalone .brand-dot { width: 22px; height: 22px; }
</style>
</head>
<body>

  <section class="ad ad-leaderboard" aria-label="Leaderboard banner">
    <div class="photo" role="img" aria-label="Photo of a businessman touching a glowing rising financial chart"></div>
    <svg class="stripe" width="1065" height="132" viewBox="0 0 1065 132" aria-hidden="true">
      <polygon points="580,0 600,0 372,132 352,132" fill="var(--orange)"/>
    </svg>
    <div class="brand"><span class="brand-dot"></span>Orvane Finance</div>
    <p class="headline">Bridging Loan Service You Can Rely On</p>
    <p class="subline">5* Rated Service &amp; No Broker Fees</p>
  </section>

  <section class="ad ad-rectangle" aria-label="Rectangle banner">
    <div class="photo" role="img" aria-label="Dimmed photo of a hand with a pen reviewing printed financial charts"></div>
    <div class="content">
      <div class="brand"><span class="brand-dot"></span>Orvane Finance</div>
      <p class="headline">Bridging Loan Service You Can Rely On</p>
      <p class="subline">5* Rated Service &amp; No Broker Fees</p>
      <p class="phone">
        <svg width="16" height="16" viewBox="0 0 24 24" aria-hidden="true"><path fill="var(--white)" d="M6.6 10.8a15.1 15.1 0 0 0 6.6 6.6l2.2-2.2c.3-.3.7-.4 1-.2 1.1.4 2.3.6 3.6.6.6 0 1 .4 1 1V20c0 .6-.4 1-1 1A17 17 0 0 1 3 4c0-.6.4-1 1-1h3.5c.6 0 1 .4 1 1 0 1.3.2 2.5.6 3.6.1.3 0 .7-.2 1z"/></svg>
        +1 555 010 0199
      </p>
    </div>
  </section>

  <section class="ad ad-skyscraper" aria-label="Skyscraper banner">
    <svg class="corner" width="72" height="72" viewBox="0 0 72 72" aria-hidden="true">
      <polygon points="12,0 72,0 72,72 0,54" fill="var(--orange)"/>
    </svg>
    <div class="brand"><span class="brand-dot"></span>Orvane Finance</div>
    <p class="headline">Bridging Loan Service You Can Rely On</p>
    <p class="subline">5* Rated Service &amp; No Broker Fees</p>
    <div class="dots-area" role="img" aria-label="White dot pattern forming a triangle"></div>
    <svg class="accent" width="260" height="180" viewBox="0 0 260 180" aria-hidden="true">
      <polygon points="260,0 200,180 0,180" fill="var(--orange)"/>
    </svg>
    <div class="person" role="img" aria-label="Photo of a smiling man in a light blue shirt holding a laptop"></div>
  </section>

  <div class="brand brand-standalone"><span class="brand-dot"></span>Orvane Finance</div>

</body>
</html>
```